The name of my company is Tolmen Refacing LLC and I would like the sub text to say "Cabinet Refacing and Countertops". Have my name Dorian Tolmen, Owner / Sales, contact info: Cell: 360-555-0147 / Email: dorian.tolmen@quenmail.com

Simple, Clean, and Organized. With colors that will appeal to the eye.

Target Market(s)

Houses and Apartments

Industry/Entity Type

Cabinet Refacing

Contact Information for Business Card

Company name and sub text Dorian Tolmen - Owner / Sales, my cell phone number and email

Requirements
Must have
• Business name, my name / position, and my contact info
Nice to have
• Simple. Organized. Appealing to the eye

```html
<!DOCTYPE html>
<html lang="en">
<head>
<meta charset="utf-8">
<title>Tolmen Refacing, LLC — Business Card</title>
<link rel="stylesheet" href="https://fonts.googleapis.com/css2?family=Raleway:wght@300&family=Didact+Gothic&family=Lato:wght@400;700&display=swap">
<style>
  :root {
    --bg: #e0e0e0;
    --card: #ffffff;
    --brand-blue: #4a6fb8;
    --brand-grey: #8a93ae;
    --ink: #333333;
    --ink-soft: #444444;
  }
  * { margin: 0; padding: 0; box-sizing: border-box; }
  html, body {
    width: 1200px; height: 1200px; overflow: hidden;
    background: var(--bg);
  }
  .stage { position: relative; width: 1200px; height: 1200px; }
  .card {
    position: absolute;
    background: var(--card);
    box-shadow: 0 6px 14px rgba(0,0,0,0.35);
    overflow: hidden;
  }
  .card--front { left: 188px; top: 90px; width: 823px; height: 474px; }
  .card--back  { left: 185px; top: 635px; width: 829px; height: 474px; }
  .card__band {
    position: absolute; left: 0; right: 0; bottom: 0; height: 19px;
    background: var(--brand-blue);
  }
  .row {
    position: absolute; left: 0; right: 0;
    text-align: center; white-space: nowrap;
  }
  .brand-mark {
    position: absolute; left: 50%;
    border-radius: 50%;
    background: var(--brand-blue);
    transform: translateX(-50%);
  }
  .card--front .brand-mark { top: 48px; width: 92px; height: 92px; }
  .card--back .brand-mark { top: 110px; width: 104px; height: 104px; }
  .brand-name {
    font-family: "Raleway", sans-serif; font-weight: 300;
    color: var(--brand-grey); letter-spacing: 1px;
  }
  .card--front .brand-name { top: 166px; font-size: 50px; line-height: 56px; }
  .card--back .brand-name { top: 233px; font-size: 56px; line-height: 62px; }
  .tagline {
    font-family: "Didact Gothic", sans-serif; color: var(--ink);
    letter-spacing: 0.5px;
  }
  .card--front .tagline { top: 224px; font-size: 24px; line-height: 30px; }
  .card--back .tagline { top: 302px; font-size: 27px; line-height: 34px; }
  .person-name {
    top: 304px; font-family: "Lato", sans-serif; font-weight: 700;
    font-size: 40px; line-height: 44px; color: var(--brand-blue);
  }
  .person-role {
    top: 352px; font-family: "Lato", sans-serif; font-size: 20px;
    line-height: 24px; color: var(--ink-soft); letter-spacing: 0.5px;
  }
  .divider {
    position: absolute; left: 175px; width: 474px; top: 389px;
    height: 2px; background: var(--brand-blue);
  }
  .contact {
    top: 412px; font-family: "Lato", sans-serif; font-size: 17px;
    line-height: 22px; color: var(--ink-soft);
  }
  .contact__label { color: var(--brand-blue); font-weight: 700; }
  .contact__sep { margin: 0 10px; }
</style>
</head>
<body>
<main class="stage">
  <section class="card card--front">
    <div class="brand-mark"></div>
    <div class="row brand-name">TOLMEN REFACING, LLC</div>
    <div class="row tagline">Cabinets and Countertops</div>
    <div class="row person-name">DORIAN TOLMEN</div>
    <div class="row person-role">OWNER &nbsp;I&nbsp; SALES</div>
    <div class="divider"></div>
    <div class="row contact">
      <span class="contact__label">Cell:</span> 360-555-0147<span class="contact__sep">I</span><span class="contact__label">Email:</span> dorian.tolmen@quenmail.com
    </div>
    <div class="card__band"></div>
  </section>

  <section class="card card--back">
    <div class="brand-mark"></div>
    <div class="row brand-name">TOLMEN REFACING, LLC</div>
    <div class="row tagline">Cabinets and Countertops</div>
    <div class="card__band"></div>
  </section>
</main>
</body>
</html>
```